LUMEN Environmental needs an upgrade to its current business cards design

We need an upgrade to our current business cards design, where the LUMEN acronym is included, as possible and not being overloaded.
LUMEN Environmental is an Environmental Consultancy Firm based in Sydney.
We would like to see creative designs different from the standard type of business cards (for example, rounded edges, different to standard size of common business cards.

Target Market(s)

industrial companies (oil & gas, petrochemical, mining, insolvency, finance and manufacturing), developers, architect firms, law firms.

Industry/Entity Type

Business

Contact Information for Business Card

logos (brand and acronym), if they don't appear overloaded.
name
role
name of company (LUMEN Environmental),
address (Level 4, Suite 4B, 72-76 Wrenfield Street, Marlow Vale, NSW, 2093) landline (02 7314 2286)
mobile (staff member)
email (staff member) and
website (www.lumenverda.example).
Include: Contaminated Land, Site Remediation, Groundwater Assessment, Health and Ecological Risk Assessments, Acid Sulfate Soils, Waste Classification.

Font styles to use
Serif
Sans Serif

Requirements
Must have
• A creative design different to the standard type of business cards.
Nice to have
• Rounded edges
• Different size of business cards rather than the standard size.
Should not have
• Preferable not to use white colour background, unless it is required from a creative design proposed.
• Not an overloaded design.
• Avoid black colours

```html
<!DOCTYPE html>
<html lang="en">
<head>
<meta charset="utf-8">
<title>LUMEN Environmental – Business Card</title>
<link href="https://fonts.googleapis.com/css2?family=Lato:wght@400;700;900&display=swap" rel="stylesheet">
<style>
  :root {
    --page-bg: #d9d4cc;
    --card-top: #eef0f1;
    --card-mid: #e3e6e8;
    --card-warm: #ecdfe0;
    --green: #5aa23a;
    --green-dark: #3f7f26;
    --green-light: #7ab84f;
    --ink: #3a3a3c;
    --ink-soft: #555557;
    --swoosh: #48474a;
    --web-text: #e9efe4;
  }
  * { margin: 0; padding: 0; box-sizing: border-box; }
  html, body {
    width: 1200px; height: 970px; overflow: hidden;
    background: var(--page-bg);
    font-family: "Lato", Arial, sans-serif;
  }
  .stage { position: relative; width: 1200px; height: 970px; }
  .card {
    position: absolute; left: 100px; top: 201px;
    width: 1000px; height: 568px;
    border-radius: 30px; overflow: hidden;
    background: linear-gradient(160deg, var(--card-top) 0%, var(--card-mid) 55%, var(--card-warm) 80%, var(--card-mid) 100%);
    box-shadow: 0 14px 40px rgba(0,0,0,.18);
  }
  .card-wave { position: absolute; left: 0; top: 0; width: 1000px; height: 568px; }
  .person { position: absolute; left: 62px; top: 70px; }
  .person-name {
    font-size: 33px; font-weight: 700; color: var(--green);
    letter-spacing: .5px; line-height: 1.05;
  }
  .person-role { font-size: 27px; color: var(--ink-soft); line-height: 1.2; }
  .contacts { position: absolute; left: 62px; top: 196px; list-style: none; }
  .contacts li {
    display: flex; align-items: center; gap: 14px;
    font-size: 29px; color: var(--ink); height: 40px;
  }
  .contacts li.email { font-size: 27px; }
  .contacts svg { width: 26px; height: 26px; flex: none; fill: var(--green); }
  .address {
    position: absolute; left: 64px; top: 344px;
    font-size: 25px; line-height: 36px; color: var(--ink-soft);
  }
  .brand { position: absolute; right: 64px; top: 52px; text-align: right; color: var(--ink); font-weight: 900; }
  .brand-name { font-size: 128px; line-height: 1; letter-spacing: 2px; }
  .brand-sub { font-size: 34px; letter-spacing: 6.5px; line-height: 1.1; margin-top: 4px; }
  .website {
    position: absolute; left: 64px; bottom: 26px;
    font-size: 26px; color: var(--web-text); letter-spacing: .3px;
  }
  .eco-mark { position: absolute; right: 56px; bottom: 40px; width: 112px; height: 112px; }
</style>
</head>
<body>
<main class="stage">
  <section class="card" aria-label="LUMEN Environmental business card">
    <svg class="card-wave" viewBox="0 0 1000 568" aria-hidden="true">
      <defs>
        <linearGradient id="greenBand" x1="0" y1="0" x2="0" y2="1">
          <stop offset="0" stop-color="#7ab84f"/>
          <stop offset=".5" stop-color="#5aa23a"/>
          <stop offset="1" stop-color="#3f7f26"/>
        </linearGradient>
      </defs>
      <path d="M0 430 C120 470 220 500 330 492 C470 480 560 420 700 400 C820 384 920 392 1000 398 L1000 568 L0 568 Z" fill="url(#greenBand)"/>
      <path d="M0 392 C90 440 190 492 310 498 C420 504 520 470 600 440 C520 480 420 512 300 510 C180 506 80 470 0 440 Z" fill="var(--swoosh)"/>
    </svg>

    <div class="person">
      <p class="person-name">ROWAN CASTELL</p>
      <p class="person-role">Project Engineer</p>
    </div>

    <ul class="contacts">
      <li class="landline">
        <svg viewBox="0 0 24 24" aria-hidden="true"><path d="M3 8c0-2 3-4 9-4s9 2 9 4v2h-5V8H8v2H3zM6 12h12l2 8H4z"/></svg>
        02 7314 2286
      </li>
      <li class="mobile">
        <svg viewBox="0 0 24 24" aria-hidden="true"><path d="M7 1h10a2 2 0 0 1 2 2v18a2 2 0 0 1-2 2H7a2 2 0 0 1-2-2V3a2 2 0 0 1 2-2zm0 3v13h10V4z"/></svg>
        0412 583 067
      </li>
      <li class="email">
        <svg viewBox="0 0 24 24" aria-hidden="true"><path d="M2 5h20v14H2zm2 2v.5l8 6 8-6V7zm0 3v7h16v-7l-8 6z"/></svg>
        rowan@lumenverda.example
      </li>
    </ul>

    <p class="address">Level 4, Suite 4B, 72-76 Wrenfield Street,<br>Marlow Vale, NSW, 2093</p>

    <div class="brand">
      <p class="brand-name">LUMEN</p>
      <p class="brand-sub">ENVIRONMENTAL</p>
    </div>

    <p class="website">www.lumenverda.example</p>

    <svg class="eco-mark" viewBox="0 0 112 112" role="img" aria-label="Recycling symbol">
      <circle cx="56" cy="56" r="50" fill="#dfe8d8" opacity=".75"/>
    </svg>
  </section>
</main>
</body>
</html>
```